Business Consultancy Business Card Design

Business Card design required for Business Analysis and Project Consultancy business based in Scotland.

Company Name - Brackwell Consulting

Back - Company Logo

Front Details

Euan Brackwell
07402 916 254
euan.brackwell@brackwellconsulting.example
http://www.brackwellconsulting.example

Colours should match the logo colours but I am open to design ideas.

```html
<!DOCTYPE html>
<html lang="en">
<head>
<meta charset="utf-8">
<title>Brackwell Consulting – Business Cards</title>
<link rel="stylesheet" href="https://fonts.googleapis.com/css2?family=Open+Sans:wght@400;600&display=swap">
<style>
  :root {
    --brand-blue: #009ddc;
    --brand-green: #6cb33f;
    --ink-grey: #5f6163;
    --ink-dark: #3a3a3a;
    --card-white: #ffffff;
    --stage: #ececec;
  }
  * { box-sizing: border-box; margin: 0; padding: 0; }
  html, body {
    width: 1200px;
    height: 985px;
    overflow: hidden;
    background: var(--stage);
    font-family: "Open Sans", Arial, sans-serif;
  }
  .card {
    position: absolute;
    left: 340px;
    width: 520px;
    height: 336px;
    background: var(--card-white);
    border-radius: 16px;
    overflow: hidden;
    box-shadow: 0 6px 18px rgba(0,0,0,0.18);
  }
  .card--back { top: 110px; }
  .card--front { top: 520px; }

  .brand-mark {
    position: absolute;
    border-radius: 50%;
    background: var(--brand-blue);
  }
  .card--back .brand-mark { width: 64px; height: 64px; left: 228px; top: 108px; }
  .card--back .brand-name {
    position: absolute;
    left: 0; right: 0; top: 190px;
    text-align: center;
    font-size: 26px;
    font-weight: 400;
    letter-spacing: 1px;
    color: var(--ink-grey);
    text-transform: uppercase;
  }

  .side-band { position: absolute; left: 0; top: 0; width: 70px; height: 100%; }
  .side-band__top { position: absolute; left: 0; top: 0; width: 100%; height: 112px; background: var(--brand-green); }
  .side-band__bottom { position: absolute; left: 0; top: 112px; width: 100%; bottom: 0; background: var(--brand-blue); }
  .card--front .brand-mark {
    width: 50px; height: 50px; left: 45px; top: 80px;
    border: 5px solid var(--card-white);
  }
  .card--front .brand-name {
    position: absolute;
    left: 108px; top: 84px;
    padding-left: 12px;
    border-left: 2px solid var(--ink-grey);
    font-size: 24px;
    line-height: 30px;
    font-weight: 400;
    letter-spacing: 1px;
    color: var(--ink-grey);
    text-transform: uppercase;
  }
  .person-name {
    position: absolute;
    left: 110px; top: 128px;
    font-size: 19px;
    color: var(--brand-blue);
  }
  .name-rule {
    position: absolute;
    left: 110px; top: 156px;
    width: 380px; height: 1px;
    background: var(--brand-green);
  }
  .contact-list { position: absolute; left: 84px; top: 174px; list-style: none; }
  .contact-list li {
    display: flex; align-items: center; gap: 10px;
    height: 22px;
    font-size: 13px;
    color: var(--ink-dark);
  }
  .contact-icon {
    width: 16px; height: 16px;
    border-radius: 3px;
    background: var(--brand-green);
    display: flex; align-items: center; justify-content: center;
    color: var(--card-white);
    font-size: 11px; font-weight: 600;
  }
  .contact-icon svg { width: 11px; height: 11px; }
</style>
</head>
<body>
  <section class="card card--back" aria-label="Card back">
    <div class="brand-mark" aria-hidden="true"></div>
    <p class="brand-name">Brackwell Consulting</p>
  </section>

  <section class="card card--front" aria-label="Card front">
    <div class="side-band" aria-hidden="true">
      <div class="side-band__top"></div>
      <div class="side-band__bottom"></div>
    </div>
    <div class="brand-mark" aria-hidden="true"></div>
    <p class="brand-name">Brackwell Consulting</p>
    <p class="person-name">Euan Brackwell</p>
    <div class="name-rule" aria-hidden="true"></div>
    <ul class="contact-list">
      <li>
        <span class="contact-icon" aria-hidden="true">
          <svg viewBox="0 0 24 24"><path fill="#fff" d="M6.6 10.8a15 15 0 0 0 6.6 6.6l2.2-2.2c.3-.3.7-.4 1-.2 1.1.4 2.3.6 3.6.6.6 0 1 .4 1 1V20c0 .6-.4 1-1 1A17 17 0 0 1 3 4c0-.6.4-1 1-1h3.5c.6 0 1 .4 1 1 0 1.3.2 2.5.6 3.6.1.3 0 .7-.2 1z"/></svg>
        </span>
        07402 916 254
      </li>
      <li><span class="contact-icon" aria-hidden="true">@</span>euan.brackwell@brackwellconsulting.example</li>
      <li>
        <span class="contact-icon" aria-hidden="true">
          <svg viewBox="0 0 24 24" fill="none" stroke="#fff" stroke-width="2"><circle cx="12" cy="12" r="9"/><path d="M3 12h18M12 3c3 3 3 15 0 18M12 3c-3 3-3 15 0 18"/></svg>
        </span>
        http://www.brackwellconsulting.example
      </li>
    </ul>
  </section>
</body>
</html>
```